Poster Design job - 11"x17" Poster for a Treasure Hunt

Summary:
This project is for a poster that will be used to promote a community treasure hunt for kids aged 9-14. This will be the 13th year we have run the treasure hunt. See the files for previous posters we have used (all from PixelHive).
***Please thoroughly read below before embarking on this project.
We loved everything about the 2012 design, particularly how all of the elements seem to belong exactly where they are on the poster. Previous years designs just had text blocks thrown on top of a background image which doesn't make a for a good poster; if within a few seconds you don’t have an idea about what even the poster is promoting, and if you can’t read every part of the poster from 6 feet away, the poster isn't working. Some of our other favorite posters for you to see are from 2012, 2016, and 2017 (attached).
Please make the Ridgeway Quest Seekers logo a featured part of the design. See the 2012 poster winner where the logo was right at the top and very prominent.
Style: Scary, but remember the event is for children 9-14years old. The title of the hunt this year is "The Dreadful Saga of Bone Masts"
We want the Mexican Pirate to look scary with the following elements:
- the time period is the Late 1700s
- Use the pirate pic attached as a starting point to create the mexican pirate. That pic is only meant as a reference. Do not copy this pic direclty as there are probably copyrights on it.
- have a scary looking pirate ship in the background with a skull on its flag.
Poster must contain these texts:
event name: "The Dreadful Saga of Bone Masts"
"Be the First Team to unravel the mystery of the Montrose Hoard and you will find a hidden Treasure chest and claim a FANTASTIC PRIZE!"
"Youth Ages 9-14 are able to participate.
"Team Applications are available on Sept 1st and due ASAP"
"Space is limited to the first 50 teams"
"Presented by Tom Wexley of Nest Homefinders and Dr. Neil Forst of Ridgeway Orthodontics"
"WWW.RIDGEQUESTKIDS.EXAMPLE"
**Must include on the poster the logos of Tom Wexley, Ridgeway Orthodontics, and Ridgeway Quest Seekers, event date of oct 13 2018.
_____
Remember, we want scary, but NOT gross and gruesome as this is for kids 9-14. Some of the poster submissions from previous years were way too gruesome with blood and gore. Do keep in mind this event is for children. For good examples, see the previous years posters attached.

```html
<!DOCTYPE html>
<html lang="en">
<head>
<meta charset="utf-8">
<title>The Dreadful Saga of Bone Masts — Ridgeway Quest Seekers</title>
<link rel="stylesheet" href="https://fonts.googleapis.com/css2?family=Creepster&family=Cinzel:wght@600&family=Arimo:wght@700&display=swap">
<style>
  :root {
    --night: #0f1416;
    --fog: #3a4548;
    --moon: #d9dcc8;
    --ribbon: #8e1b1b;
    --ribbon-dark: #2a0606;
    --swoosh: #3b0c0c;
    --cream: #f3e6d2;
    --white: #ffffff;
    --parchment: #d9b77c;
    --ink: #0b0b0b;
    --pirate: #4a4a44;
  }
  * { margin: 0; padding: 0; box-sizing: border-box; }
  html, body { width: 799px; height: 1200px; overflow: hidden; background: var(--night); }
  .poster {
    position: relative; width: 799px; height: 1200px; overflow: hidden;
    background:
      radial-gradient(circle at 62px 62px, var(--moon) 0 40px, rgba(217,220,200,.35) 46px, transparent 140px),
      linear-gradient(180deg, #2c3538 0%, #1b2326 40%, #222a2c 75%, var(--night) 100%);
  }
  .scene-art { position: absolute; inset: 0; }
  .pirate-art {
    position: absolute; left: 370px; top: 200px; width: 429px; height: 800px;
    background: radial-gradient(ellipse at 55% 40%, var(--pirate) 0%, #2b2a27 55%, transparent 78%);
  }
  .brand {
    position: absolute; top: 38px; left: 0; width: 100%; text-align: center;
    font-family: "Cinzel", serif; font-weight: 600; color: var(--white);
    letter-spacing: 2px; line-height: 1.1;
  }
  .brand-small { font-size: 20px; }
  .brand-large { font-size: 40px; }
  .swoosh { position: absolute; background: var(--swoosh); }
  .swoosh-a { left: 40px; top: 380px; width: 520px; height: 70px; transform: rotate(-38deg); }
  .swoosh-b { left: 10px; top: 600px; width: 520px; height: 60px; transform: rotate(-38deg); }
  .ribbon { position: absolute; }
  .ribbon svg { position: absolute; inset: 0; width: 100%; height: 100%; }
  .ribbon-text {
    position: relative; height: 100%; display: flex; align-items: center; justify-content: center;
    text-align: center; font-family: "Creepster", cursive; color: var(--cream);
    text-shadow: 2px 2px 0 var(--ribbon-dark);
  }
  .ribbon-title { left: 46px; top: 373px; width: 400px; height: 80px; transform: rotate(14deg); }
  .ribbon-title .ribbon-text { font-size: 34px; letter-spacing: 1px; }
  .ribbon-name { left: 10px; top: 455px; width: 460px; height: 96px; transform: rotate(6deg); }
  .ribbon-name .ribbon-text { font-size: 62px; }
  .ribbon-name .small { font-size: 38px; margin-right: 12px; }
  .ribbon-mission { left: -16px; top: 640px; width: 540px; height: 124px; transform: rotate(-10deg); }
  .ribbon-mission .ribbon-text { font-size: 17px; line-height: 1.25; padding: 0 40px; }
  .ribbon-url { left: 30px; top: 840px; width: 446px; height: 90px; transform: rotate(-23deg); }
  .ribbon-url .ribbon-text { font-size: 24px; }
  .event-date {
    position: absolute; left: 616px; top: 881px; width: 181px; height: 112px;
    background: var(--parchment); border: 2px solid #8a6a38;
    display: flex; align-items: center; justify-content: center; text-align: center;
    font-family: "Arimo", sans-serif; font-weight: 700; font-size: 25px; line-height: 1.2; color: var(--ink);
  }
  .details {
    position: absolute; left: 0; top: 1002px; width: 800px; text-align: center; list-style: none;
    font-family: "Arimo", sans-serif; font-weight: 700; font-size: 18px; line-height: 28.5px; color: var(--white);
  }
  .sponsor {
    position: absolute; background: var(--white); display: flex; align-items: center; justify-content: center;
    text-align: center; font-family: "Arimo", sans-serif; font-weight: 700; color: #1f3b7a;
  }
  .sponsor-realtor { left: 38px; top: 1062px; width: 72px; height: 78px; font-size: 13px; }
  .sponsor-ortho { left: 662px; top: 1078px; width: 130px; height: 62px; font-size: 14px; line-height: 1.2; }
</style>
</head>
<body>
<main class="poster">
  <div class="scene-art" role="img" aria-label="Moonlit graveyard at night with bare trees, bats and a shadowy crowd of undead pirates"></div>
  <div class="pirate-art" role="img" aria-label="Illustrated skeletal pirate in a wide sombrero holding a cutlass"></div>

  <header class="brand">
    <div class="brand-small">RIDGEWAY</div>
    <div class="brand-large">QUEST SEEKERS</div>
  </header>

  <div class="swoosh swoosh-a"></div>
  <div class="swoosh swoosh-b"></div>

  <div class="ribbon ribbon-title">
    <svg viewBox="0 0 400 80" preserveAspectRatio="none"><polygon points="0,0 400,0 380,40 400,80 0,80 20,40" fill="var(--ribbon)" stroke="var(--ribbon-dark)" stroke-width="4"/></svg>
    <h1 class="ribbon-text">THE DREADFUL SAGA</h1>
  </div>

  <div class="ribbon ribbon-name">
    <svg viewBox="0 0 460 96" preserveAspectRatio="none"><polygon points="0,0 460,0 440,48 460,96 0,96 20,48" fill="var(--ribbon)" stroke="var(--ribbon-dark)" stroke-width="4"/></svg>
    <div class="ribbon-text"><span class="small">OF</span>BONE MASTS</div>
  </div>

  <div class="ribbon ribbon-mission">
    <svg viewBox="0 0 540 124" preserveAspectRatio="none"><polygon points="0,0 540,0 515,62 540,124 0,124 25,62" fill="var(--ribbon)" stroke="var(--ribbon-dark)" stroke-width="4"/></svg>
    <p class="ribbon-text">BE THE FIRST TEAM TO UNRAVEL THE MYSTERY OF THE MONTROSE HOARD AND YOU WILL FIND A HIDDEN TREASURE CHEST AND CLAIM A FANTASTIC PRIZE!</p>
  </div>

  <div class="ribbon ribbon-url">
    <svg viewBox="0 0 446 90" preserveAspectRatio="none"><polygon points="0,0 446,0 424,45 446,90 0,90 22,45" fill="var(--ribbon)" stroke="var(--ribbon-dark)" stroke-width="4"/></svg>
    <p class="ribbon-text">WWW.RIDGEQUESTKIDS.EXAMPLE</p>
  </div>

  <div class="event-date">Event date<br>of<br>Oct 13, 2018</div>

  <ul class="details">
    <li>· Youth Ages 9-14 are able to participate.</li>
    <li>· Team Applications are available on Sept 1st and due ASAP</li>
    <li>· Space is limited to the first 50 teams</li>
    <li>Presented by Tom Wexley of Nest Homefinders</li>
    <li>and Dr. Neil Forst of Ridgeway Orthodontics</li>
  </ul>

  <div class="sponsor sponsor-realtor">Tom Wexley</div>
  <div class="sponsor sponsor-ortho">Ridgeway Orthodontics</div>
</main>
</body>
</html>
```